Construction machinery rental / heavy equipment rental needs a nice billboard

We need a billboard for our company.
We rent out construction machinery such as excavators, wheel loaders, wheel dumpers and so on...

I would like an elegant, simple, dark design.
Colors: black yellow grey white

The following must be on the billboard:
Logo
phone number: 076 / 913 58 40
website: www.geraetepark-lorvento.ch
the machines I rent out: Bagger bis 10T, Radlader, Dumper, Raupenkipper

the font in the logo is: Square 721

Final format 2950 x 1900mm
I have uploaded pictures:
"Excavator 1-6" are my pictures, which can be used
"Sample 1-4" are pictures whose style I like
"Billboard" are billboards which I like

Requirements
Must have
• The following must be on the billboard: Logo phone number: 076 / 913 58 40 website: www.geraetepark-lorvento.ch the machines I rent out: Bagger bis 10T, Radlader, Dumper, Raupenkipper

```html
<!DOCTYPE html>
<html lang="de">
<head>
<meta charset="utf-8">
<title>Lorvento – Billboard Baumaschinenvermietung</title>
<link rel="stylesheet" href="https://fonts.googleapis.com/css2?family=Exo+2:ital,wght@0,800;1,700;1,800&family=Oswald:wght@500&family=Poppins:ital,wght@1,600;1,700&display=swap">
<style>
  :root {
    --page-bg: #d8fcfd;
    --board-black: #000000;
    --gold: #c8b33a;
    --gold-light: #e2cd4e;
    --white: #ffffff;
    --photo-dark: #0c0d0f;
    --photo-mid: #2a2c30;
    --photo-rust: #6a4a2c;
  }
  * { margin: 0; padding: 0; box-sizing: border-box; }
  html, body {
    width: 875px;
    height: 1200px;
    overflow: hidden;
    background: var(--page-bg);
  }
  .billboard {
    position: absolute;
    left: 40px;
    top: 344px;
    width: 795px;
    height: 512px;
    background: var(--board-black);
    box-shadow: 0 10px 28px rgba(0, 0, 0, 0.28);
    overflow: hidden;
    color: var(--white);
  }
  .machine-photo {
    position: absolute;
    left: 369px;
    top: 0;
    width: 426px;
    height: 440px;
    background:
      radial-gradient(ellipse 55% 40% at 35% 82%, var(--photo-rust) 0%, transparent 60%),
      radial-gradient(ellipse 70% 60% at 60% 50%, var(--photo-mid) 0%, var(--photo-dark) 65%, var(--board-black) 100%);
  }
  .brand {
    position: absolute;
    left: 51px;
    top: 50px;
    display: flex;
    align-items: center;
    gap: 12px;
  }
  .brand-mark {
    width: 22px;
    height: 22px;
    background: var(--gold);
  }
  .brand-name {
    font-family: "Exo 2", sans-serif;
    font-weight: 800;
    font-size: 46px;
    letter-spacing: 1px;
    color: var(--gold);
    line-height: 1;
  }
  .headline {
    position: absolute;
    left: 44px;
    top: 128px;
    font-family: "Oswald", sans-serif;
    font-weight: 500;
    font-size: 40px;
    line-height: 1;
    color: var(--gold);
    transform: skewX(-6deg);
    white-space: nowrap;
  }
  .machine-list {
    position: absolute;
    left: 40px;
    top: 192px;
    list-style: none;
  }
  .machine-item {
    display: flex;
    align-items: center;
    height: 54px;
    font-family: "Exo 2", sans-serif;
    font-style: italic;
    font-weight: 800;
    font-size: 31px;
    letter-spacing: 1px;
    white-space: nowrap;
  }
  .machine-item svg { width: 28px; height: 20px; margin-right: 20px; flex: none; }
  .contact-phone {
    position: absolute;
    left: 40px;
    top: 420px;
    display: flex;
    align-items: center;
    font-family: "Poppins", sans-serif;
    font-style: italic;
    font-weight: 700;
    font-size: 36px;
    line-height: 1;
    white-space: nowrap;
  }
  .contact-phone svg { width: 30px; height: 30px; margin-right: 17px; flex: none; }
  .contact-web {
    position: absolute;
    left: 389px;
    top: 444px;
    font-family: "Poppins", sans-serif;
    font-style: italic;
    font-weight: 600;
    font-size: 18px;
    white-space: nowrap;
  }
  .contact-web .web-domain { color: var(--gold); }
</style>
</head>
<body>
  <section class="billboard">
    <div class="machine-photo" role="img" aria-label="Foto eines Minibaggers mit Schaufel und Planierschild vor dunklem Hintergrund"></div>

    <div class="brand">
      <span class="brand-mark"></span>
      <span class="brand-name">LORVENTO</span>
    </div>

    <h1 class="headline">THE MACHINES I RENT OUT</h1>

    <ul class="machine-list">
      <li class="machine-item">
        <svg viewBox="0 0 28 20" aria-hidden="true"><path d="M2 2h6l7 8-7 8H2l7-8z M13 2h6l7 8-7 8h-6l7-8z" fill="var(--gold)"/></svg>
        BAGGER BIS 10T
      </li>
      <li class="machine-item">
        <svg viewBox="0 0 28 20" aria-hidden="true"><path d="M2 2h6l7 8-7 8H2l7-8z M13 2h6l7 8-7 8h-6l7-8z" fill="var(--gold)"/></svg>
        RADLADER
      </li>
      <li class="machine-item">
        <svg viewBox="0 0 28 20" aria-hidden="true"><path d="M2 2h6l7 8-7 8H2l7-8z M13 2h6l7 8-7 8h-6l7-8z" fill="var(--gold)"/></svg>
        DUMPER
      </li>
      <li class="machine-item">
        <svg viewBox="0 0 28 20" aria-hidden="true"><path d="M2 2h6l7 8-7 8H2l7-8z M13 2h6l7 8-7 8h-6l7-8z" fill="var(--gold)"/></svg>
        RAUPENKIPPER
      </li>
    </ul>

    <div class="contact-phone">
      <svg viewBox="0 0 30 30" aria-hidden="true">
        <circle cx="15" cy="15" r="15" fill="var(--gold)"/>
        <path d="M10.5 8.2c.6-.4 1.3-.3 1.7.3l1.6 2.4c.4.6.3 1.3-.2 1.7l-1 .8c.7 1.8 2.2 3.3 4 4.1l.8-1c.4-.5 1.1-.6 1.7-.2l2.4 1.6c.6.4.7 1.1.3 1.7l-.9 1.3c-.5.7-1.4 1-2.2.8-4.6-1.2-8.1-4.8-9.3-9.4-.2-.8.1-1.7.8-2.2z" fill="var(--board-black)"/>
      </svg>
      076 / 913 58 40
    </div>

    <p class="contact-web">www.<span class="web-domain">geraetepark-lorvento</span>.ch</p>
  </section>
</body>
</html>
```